Following list to be designed:

1. A4 Letter Head

Must comprise of:
BRISK HARBOR and its LOGO
Address: No.41, 2F, Telvin Court, Marlow Lane, Upper Fennel Gardens, Bangalore 560 078
Tel: 080 41927380
Fax: 080 41927381
Mail: hello@briskharbor.example

Color of wordings to be in the lighter shade of blue and brighter shade of blue.

2. A4 Envelope

Must comprise of:
BRISK HARBOR and its LOGO
Tel: 080 41927380
Fax: 080 41927381

3. Postal Envelope

Must comprise of:
BRISK HARBOR and its LOGO
Tel: 080 41927380
Fax: 080 41927381

4. Business Card

Must comprise of:
Ravi Menon
Managing Partner
Cell: +91 9847162053
Mail: ravimenon@briskharbor.example
Tel: 080 41927380
Fax: 080 41927381

5. A4 Letter Head

Must comprise of:
BRISK HARBOR CORP. (wording) and BRISK HARBOR LOGO (only blue ribbon)

Blue ribbon (BRISK HARBOR LOGO) may be placed on Left Top Corner of the A4 Letter Head
and BRISK HARBOR CORP. (wording) to be placed on Right Top Corner of the A4 Letter Head

Tel: 080 41927380
Fax: 080 41927381

6. . A4 Envelope

Must comprise of:

Blue ribbon (BRISK HARBOR LOGO) may be placed on Left Top Corner of the A4 Envelope
and BRISK HARBOR CORP. (wording) to be placed on Right Top Corner of the A4 Envelope
Tel: 080 41927380
Fax: 080 41927381

Target Market(s)

Top IT/ITES Organizations

Industry/Entity Type

Real Estate Development

Font styles to use
Serif
Sans Serif

Colors
33a6d7
0792cd
85cae6

Requirements
Should not have
• Playful font and color

```html
<!DOCTYPE html>
<html lang="en">
<head>
<meta charset="utf-8">
<title>Brisk Harbor — Business Card</title>
<link rel="stylesheet" href="https://fonts.googleapis.com/css2?family=PT+Sans:wght@400;700&display=swap">
<style>
  :root {
    --page-bg: #eceeef;
    --card-bg: #dfe2e1;
    --panel-dark: #5c6a74;
    --panel-light: #85cae6;
    --brand-blue: #0792cd;
    --mid-blue: #33a6d7;
    --name-blue: #1c4f86;
    --ink: #2a2d30;
    --text: #3b3e40;
  }
  html, body {
    margin: 0;
    width: 1200px;
    height: 969px;
    overflow: hidden;
    background: var(--page-bg);
    font-family: "PT Sans", Arial, sans-serif;
  }
  .business-card {
    position: absolute;
    left: 163px;
    top: 237px;
    width: 873px;
    height: 495px;
    background: var(--card-bg);
    box-shadow: 0 6px 24px rgba(0,0,0,0.12);
    overflow: hidden;
  }
  .brand-panel {
    position: absolute;
    left: 0;
    top: 0;
    width: 367px;
    height: 100%;
    background: linear-gradient(160deg, var(--panel-dark) 0%, #6f8596 55%, var(--mid-blue) 100%);
  }
  .wordmark {
    position: absolute;
    left: 415px;
    top: 40px;
    margin: 0;
    font-size: 50px;
    font-weight: 700;
    letter-spacing: 2px;
    color: var(--ink);
    line-height: 1;
  }
  .holder-name {
    position: absolute;
    left: 414px;
    top: 124px;
    margin: 0;
    font-size: 30px;
    font-weight: 700;
    letter-spacing: 0.5px;
    color: var(--name-blue);
  }
  .holder-role {
    position: absolute;
    left: 414px;
    top: 170px;
    margin: 0;
    font-size: 23px;
    color: var(--text);
  }
  .contact-list {
    position: absolute;
    left: 414px;
    top: 218px;
    margin: 0;
    padding: 0;
    list-style: none;
  }
  .contact-item {
    display: flex;
    align-items: center;
    height: 33px;
    font-size: 22px;
    color: var(--text);
  }
  .contact-icon {
    width: 22px;
    height: 22px;
    margin-right: 13px;
    fill: var(--name-blue);
    flex: none;
  }
  .office-address {
    position: absolute;
    left: 414px;
    top: 368px;
    margin: 0;
    font-style: normal;
    font-size: 22px;
    line-height: 30.5px;
    color: var(--text);
  }
</style>
</head>
<body>
  <div class="business-card">
    <div class="brand-panel"></div>

    <p class="wordmark">BRISK HARBOR</p>

    <h1 class="holder-name">RAVI MENON</h1>
    <p class="holder-role">Managing Partner</p>

    <ul class="contact-list">
      <li class="contact-item">
        <svg class="contact-icon" viewBox="0 0 24 24" aria-hidden="true"><path d="M6.6 10.8a15.1 15.1 0 0 0 6.6 6.6l2.2-2.2c.3-.3.7-.4 1-.2 1.1.4 2.3.6 3.6.6.6 0 1 .4 1 1V20c0 .6-.4 1-1 1A17 17 0 0 1 3 4c0-.6.4-1 1-1h3.5c.6 0 1 .4 1 1 0 1.3.2 2.5.6 3.6.1.3 0 .7-.2 1z"/></svg>
        080 41927380
      </li>
      <li class="contact-item">
        <svg class="contact-icon" viewBox="0 0 24 24" aria-hidden="true"><path d="M7 1h10a2 2 0 0 1 2 2v18a2 2 0 0 1-2 2H7a2 2 0 0 1-2-2V3a2 2 0 0 1 2-2zm0 3v14h10V4zm5 15.5a1.2 1.2 0 1 0 0 2.4 1.2 1.2 0 0 0 0-2.4z"/></svg>
        +91 9847162053
      </li>
      <li class="contact-item">
        <svg class="contact-icon" viewBox="0 0 24 24" aria-hidden="true"><path d="M6 2h9l3 3v4H6zM3 10h18a2 2 0 0 1 2 2v6h-4v4H5v-4H1v-6a2 2 0 0 1 2-2zm4 6v4h10v-4z"/></svg>
        080 41927381
      </li>
      <li class="contact-item">
        <svg class="contact-icon" viewBox="0 0 24 24" aria-hidden="true"><path d="M2 5h20v14H2zm2 2v.4l8 5.2 8-5.2V7zm0 2.8V17h16V9.8l-8 5.2z"/></svg>
        ravimenon@briskharbor.example
      </li>
    </ul>

    <address class="office-address">
      No.41, 2F, Telvin Court<br>
      Marlow Lane, Upper Fennel Gardens<br>
      Bangalore 560 078
    </address>
  </div>
</body>
</html>
```